Podiatry clinic requires a modern revamp and editing of existing website.

I would like a fresh new look and updated information for my current business website. An easy to navigate site with prominent address and phone number for call to action. We are a podiatry clinic that focuses on general and sports podiatry.
I would like 4 pages; including Home page, About Us, Services & Contact.
www.harbourlanefootcare.com

Target Market(s)

Active working professionals.

Industry/Entity Type

Medical

Coding

Coded - Design and coding required

Number of Pages Required

4 page

Font styles to use
Sans Serif

Colors
6b449b

Requirements
Must have
• A modern look with logo and active images; clean and uncluttered. Visible phone number and address for call to action.
• 4 pages - Home, About Us, Services, Contact.
• Home page - update address & service logos.
• About Us - update of personal information.
• Services - Revamp of existing page.
• Contact page to include Google map, email & phone number.
Nice to have
• Ability to add content easily; eg. a blog or adding video onto Home page.
• Link to Facebook page.

```html
<!DOCTYPE html>
<html lang="en">
<head>
<meta charset="utf-8">
<title>Harbour Lane Foot Care</title>
<link rel="stylesheet" href="https://fonts.googleapis.com/css2?family=Cabin:ital,wght@0,500;0,700;1,600&family=Open+Sans:wght@400;600;700&display=swap">
<style>
:root{
  --purple:#6b449b;
  --purple-deep:#4f3182;
  --purple-soft:#8d6fc2;
  --lilac:#a58bd1;
  --ink:#2b2b2b;
  --text:#4a4a4a;
  --muted:#777;
  --dark:#1c1c1c;
  --nav:#2c2c2c;
  --frame:#e6e6e6;
  --wash:#f1f4f8;
  --white:#fff;
}
*{box-sizing:border-box;margin:0;padding:0}
html,body{width:687px;height:1200px;overflow:hidden}
body{background:var(--frame);font-family:"Open Sans",sans-serif;color:var(--text);position:relative}
.page{position:absolute;left:8px;top:8px;width:671px;height:1184px;background:var(--white);overflow:hidden}
.abs{position:absolute}
.heading{font-family:"Cabin",sans-serif}

/* header */
.topbar{left:0;top:0;width:671px;height:69px;background:linear-gradient(180deg,#5a3a8c,#4b2f7a)}
.mailtab{left:424px;top:0;width:247px;height:23px;background:#7a5aad;clip-path:polygon(0 0,100% 0,96% 100%,6% 100%);color:#fff;font-size:8px;font-weight:600;display:flex;align-items:center;gap:5px;padding-left:36px}
.circle-ico{width:11px;height:11px;border:1px solid #fff;border-radius:50%;display:inline-block}
.contactline{top:46px;color:#fff;font-family:"Cabin",sans-serif;font-weight:700;font-size:10.5px;display:flex;align-items:center;gap:6px}
.logo{left:14px;top:2px;width:142px;height:80px;background:var(--purple-soft);box-shadow:0 2px 4px rgba(0,0,0,.3);z-index:5;display:flex;align-items:center;justify-content:center;gap:6px;padding:0 8px}
.logo-dot{width:12px;height:12px;border-radius:50%;background:#fff;flex:none}
.logo-name{font-family:"Cabin",sans-serif;font-weight:700;color:#fff;font-size:14px;line-height:1.15}
.nav{left:0;top:69px;width:671px;height:25px;background:rgba(35,35,35,.92);z-index:4}
.nav a{position:absolute;top:7px;color:#fff;font-family:"Cabin",sans-serif;font-weight:700;font-size:9.5px;text-decoration:none}
.nav a.active{color:#c9b6ea}
.nav a.active::after{content:"";position:absolute;left:50%;bottom:-8px;margin-left:-4px;border:4px solid transparent;border-bottom-color:#fff}

/* hero */
.hero-photo{top:69px;height:325px}
.services-card{left:470px;top:108px;width:147px;height:286px;background:#fff;border-radius:5px 5px 0 0;box-shadow:0 0 6px rgba(0,0,0,.2)}
.services-card h3{text-align:center;color:var(--purple);font-family:"Cabin",sans-serif;font-size:10px;font-weight:700;margin-top:8px}
.ribbon{left:-10px;top:32px;width:167px;height:15px;background:var(--purple);color:#fff;font-family:"Cabin",sans-serif;font-weight:700;font-size:8px;text-align:center;line-height:15px}
.card-photo{left:-10px;top:46px;width:167px;height:48px}
.card-text{font-size:6.5px;line-height:9.5px;color:var(--muted);text-align:center}
.card-rule{left:0;top:205px;width:147px;border-top:1px solid #ddd}

/* welcome */
.welcome{left:0;top:386px;width:671px;height:302px;background:var(--wash)}
.title{font-family:"Cabin",sans-serif;font-weight:700;color:var(--ink)}
.title em{font-style:normal;color:var(--purple-soft)}
.divider{height:1px;background:#ccc}
.divider-mark{width:7px;height:7px;border-radius:50%;background:var(--purple)}
.body-copy{left:33px;top:109px;width:350px;font-size:7.5px;line-height:11px;color:var(--text)}
.body-copy p{margin-bottom:11px}
.body-copy b{color:var(--purple-deep);font-weight:600}
.btn{top:248px;width:148px;height:23px;background:var(--purple-deep);color:#fff;font-family:"Cabin",sans-serif;font-weight:700;font-size:9px;display:flex;align-items:center;gap:10px;padding-left:10px;clip-path:polygon(0 0,94% 0,100% 50%,94% 100%,0 100%)}

/* form */
.form-box{left:462px;top:50px;width:178px;height:230px;background:#f7f7f7;box-shadow:0 6px 8px -4px rgba(0,0,0,.35)}
.form-head{left:447px;top:52px;width:192px;height:27px;background:var(--purple-deep);color:#fff;font-family:"Cabin",sans-serif;font-weight:700;font-size:10.5px;text-align:center;line-height:27px}
.field{left:474px;width:158px;height:18px;display:flex;gap:3px}
.field .ico{width:17px;height:18px;border:1px solid #ccc;background:#fafafa;display:flex;align-items:center;justify-content:center}
.field .in{flex:1;border:1px solid #ccc;background:#fff;font-size:6.5px;font-weight:600;color:#333;padding:5px 6px}
.submit{left:485px;top:245px;width:106px;height:16px;background:#111;color:#fff;font-size:7px;font-weight:700;text-align:center;line-height:16px}

/* testimonials */
.quote-card{top:790px;width:186px;height:100px;background:#f0f0f0;border:1px solid #ddd;border-radius:4px;padding:14px 12px 0 32px;font-size:7.5px;line-height:10.5px;color:#444}
.quote-card::before{content:"\201C";position:absolute;left:9px;top:3px;font-family:"Cabin",sans-serif;font-weight:700;font-size:28px;color:#555}
.avatar{width:54px;height:54px;border-radius:50%;border:2px solid var(--purple);background:linear-gradient(160deg,#d9d3e2,#9b8fae)}
.who{top:902px;font-family:"Cabin",sans-serif;font-style:italic;font-weight:600;font-size:10px;color:var(--ink)}
.dots{left:324px;top:943px;display:flex;gap:3px}
.dots span{width:6px;height:6px;border-radius:50%;background:#ccc}
.dots span:first-child{background:var(--purple)}

/* footer */
.footer{left:0;top:975px;width:671px;height:191px;background:var(--dark)}
.foot-logo{left:35px;top:35px;display:flex;align-items:center;gap:7px}
.foot-head{color:var(--lilac);font-family:"Cabin",sans-serif;font-weight:700;font-size:8px;top:37px}
.foot-list{color:#fff;font-size:7px;font-weight:600;line-height:10px}
.foot-item{display:flex;gap:7px;align-items:flex-start;color:#fff;font-size:7px;font-weight:600;line-height:10px}
.map{left:426px;top:33px;width:212px;height:127px;background:linear-gradient(135deg,#f1e9d2,#e4e6df 55%,#d8e3ec)}
.bottombar{left:0;top:1166px;width:671px;height:18px;background:var(--purple-deep);color:#fff;font-size:5.5px;font-weight:700;padding:6px 17px}
.socials{display:flex;gap:3px}
</style>
</head>
<body>
<div class="page">

  <!-- header -->
  <div class="abs topbar"></div>
  <div class="abs mailtab">
    <svg width="10" height="10" viewBox="0 0 10 10"><circle cx="5" cy="5" r="4.5" fill="none" stroke="#fff"/><rect x="2.5" y="3.3" width="5" height="3.4" fill="none" stroke="#fff" stroke-width=".8"/></svg>
    info@harbourlanefootcare.com
    <span class="socials" style="margin-left:12px"><span class="circle-ico"></span><span class="circle-ico"></span></span>
  </div>
  <div class="abs contactline" style="left:315px">
    <svg width="14" height="14" viewBox="0 0 14 14"><circle cx="7" cy="7" r="6.3" fill="none" stroke="#fff" stroke-width="1.2"/><path d="M4.5 4c.6-.6 1.2-.4 1.5.2l.4.8c.2.4 0 .7-.3 1 .4.9 1 1.5 1.9 1.9.3-.3.6-.5 1-.3l.8.4c.6.3.8.9.2 1.5-1.3 1.2-5.8-3.3-5.5-5.5z" fill="#fff"/></svg>
    1300 555 274
  </div>
  <div class="abs contactline" style="left:420px">
    <svg width="14" height="14" viewBox="0 0 14 14"><circle cx="7" cy="7" r="6.3" fill="none" stroke="#fff" stroke-width="1.2"/><path d="M7 3.3a2.4 2.4 0 0 1 2.4 2.4c0 1.8-2.4 4.6-2.4 4.6S4.6 7.5 4.6 5.7A2.4 2.4 0 0 1 7 3.3z" fill="#fff"/><circle cx="7" cy="5.7" r=".9" fill="#5a3a8c"/></svg>
    Suite 12 / 88 Harbour Lane Melbourne 3000
  </div>
  <div class="abs logo">
    <span class="logo-dot"></span>
    <span class="logo-name">Harbour Lane<br>Foot Care</span>
  </div>

  <!-- hero -->
  <div class="abs hero-photo" style="left:0;width:168px;background:linear-gradient(160deg,#e9ecef,#9aa7b6 45%,#c87a3a 70%,#3b4350)" role="img" aria-label="Runner's foot on a track with the ankle bones highlighted"></div>
  <div class="abs hero-photo" style="left:167px;width:168px;background:linear-gradient(180deg,#4d5560,#2d3340 40%,#6d7b8a 75%,#8b96a2)" role="img" aria-label="Group of runners on a city road, legs and shoes in view"></div>
  <div class="abs hero-photo" style="left:335px;width:137px;background:linear-gradient(180deg,#e0a85a,#b46a3a 45%,#3a3d5c 70%,#6b5b50)" role="img" aria-label="Runner on a path at sunset"></div>
  <div class="abs hero-photo" style="left:472px;width:199px;background:linear-gradient(180deg,#f0b25a,#d98a4a 50%,#7a5a4a)" role="img" aria-label="Running shoe on a warm sunset path"></div>

  <nav class="abs nav">
    <a class="active" style="left:255px" href="#">HOME</a>
    <a style="left:316px" href="#">ABOUT US</a>
    <a style="left:393px" href="#">SERVICES &#8964;</a>
    <a style="left:473px" href="#">CONTACT</a>
    <a style="left:549px" href="#">BLOG</a>
  </nav>

  <div class="abs services-card">
    <h3>OUR SERVICES</h3>
    <div class="abs ribbon">General Treatments</div>
    <div class="abs card-photo" style="background:linear-gradient(100deg,#c9cfd6,#eef0f2 50%,#d9c1b1)" role="img" aria-label="Gloved hand examining a patient's foot"></div>
    <p class="abs card-text" style="left:8px;top:104px;width:131px">At Harbour Lane Foot Care, we provide general treatments including; Nails, Corns, Callus, Warts, Skin Disorders, Heel Pain, Heel Spurs, Arch Pain-Plantar Fasciitis, Ankle Pain, Shin Splints, Knee Paint, Bunions, Hammertoes and Toe Deformities</p>
    <div class="abs card-rule"></div>
    <p class="abs heading" style="left:0;top:212px;width:147px;text-align:center;font-weight:700;font-size:8px;color:#222">Specialised Treatments</p>
    <p class="abs card-text" style="left:8px;top:223px;width:131px">Our specialised treatments including; Diabetic Management, Nail Surgery, Biomechanical Assessment, Gait Analysis, and Orthotic Therapy.</p>
  </div>

  <!-- welcome -->
  <section class="abs welcome">
    <h1 class="abs title" style="left:56px;top:40px;font-size:17.5px">Welcome to <em>Harbour Lane Foot Care</em></h1>
    <div class="abs divider" style="left:32px;top:82px;width:168px"></div>
    <div class="abs divider-mark" style="left:200px;top:79px"></div>
    <div class="abs divider" style="left:214px;top:82px;width:168px"></div>
    <div class="abs body-copy">
      <p>Harbour Lane Foot Care is a Podiatry clinic in the heart of Melbourne CBD. We are located between Elm &amp; Bay Streets in the Harbourside Business Centre.</p>
      <p>Our podiatrists are fully qualified health professionals who are able to diagnose, treat, manage or help to prevent all medical conditions that affect the feet and lower limb.</p>
      <p>We provide General Podiatry Treatment and some Specialised Services in relation to various foot conditions, including Sports Injuries, Orthotic Therapy and Nail Surgery.</p>
      <p>For Appointments or Enquiries please call us on <b>1300 555 274</b> or<br>email: <b>info@harbourlanefootcare.com</b></p>
    </div>
    <div class="abs btn" style="left:32px">
      <svg width="16" height="12" viewBox="0 0 16 12"><path d="M1 6l4 4 10-9" fill="none" stroke="#9ec7f0" stroke-width="2.4"/></svg>
      OUR SERVICES
    </div>
    <div class="abs btn" style="left:188px">
      <svg width="15" height="15" viewBox="0 0 15 15"><circle cx="7.5" cy="7.5" r="7" fill="#7e67b8"/><path d="M6 4.5v6l4.5-3z" fill="#fff"/></svg>
      TREATMENT VIDEOS
    </div>

    <div class="abs form-box"></div>
    <div class="abs form-head">Schedule an Appointment</div>
    <div class="abs field" style="top:90px"><span class="ico"><svg width="8" height="9" viewBox="0 0 8 9"><circle cx="4" cy="2.5" r="2" fill="#555"/><path d="M0 9c0-3 1.8-4 4-4s4 1 4 4z" fill="#555"/></svg></span><span class="in">NAME</span></div>
    <div class="abs field" style="top:114px"><span class="ico"><svg width="8" height="8" viewBox="0 0 8 8"><path d="M1 .8c.7-.7 1.3-.4 1.6.2l.4.9c.2.4 0 .7-.3 1 .4 1 1.1 1.7 2 2.1.3-.3.6-.5 1-.3l.9.4c.6.3.9.9.2 1.6C5.3 8.1.2 3 1 .8z" fill="#555"/></svg></span><span class="in">MOBILE PHONE</span></div>
    <div class="abs field" style="top:138px"><span class="ico" style="font-size:9px;color:#555">@</span><span class="in">EMAIL</span></div>
    <div class="abs field" style="top:162px"><span class="ico"><svg width="7" height="9" viewBox="0 0 7 9"><rect x="1" y="1" width="5" height="7" rx="2" fill="#555"/></svg></span><span class="in" style="display:flex;justify-content:space-between">INTERESTED IN <svg width="7" height="5" viewBox="0 0 7 5"><path d="M0 0h7L3.5 5z" fill="#555"/></svg></span></div>
    <div class="abs field" style="top:186px;height:56px"><span class="ico" style="height:18px"><svg width="9" height="7" viewBox="0 0 9 7"><rect x=".5" y=".5" width="8" height="6" fill="none" stroke="#555"/><path d="M.5.5l4 3.3 4-3.3" fill="none" stroke="#555"/></svg></span><span class="in">MESSAGE</span></div>
    <div class="abs submit">SUBMIT</div>
  </section>

  <!-- testimonials -->
  <h2 class="abs title" style="left:0;top:713px;width:671px;text-align:center;font-size:17px">What our patients say about <em>us</em></h2>
  <div class="abs divider" style="left:164px;top:748px;width:164px"></div>
  <div class="abs divider-mark" style="left:331px;top:745px"></div>
  <div class="abs divider" style="left:343px;top:748px;width:164px"></div>

  <div class="abs quote-card" style="left:42px">Lorem ipsum dolor sit amet, consectetu er adipiscing elit, sed diam nonummy nibh euismod tincidunt ut laoreet dolor magna aliquam erat volu. Wisi enim ad minim veniam.</div>
  <div class="abs quote-card" style="left:243px">Lorem ipsum dolor sit amet, consectetu er adipiscing elit, sed diam nonummy nibh euismod tincidunt ut laoreet dolor magna aliquam erat volu. Wisi enim ad minim veniam.</div>
  <div class="abs quote-card" style="left:444px">Lorem ipsum dolor sit amet, consectetu er adipiscing elit, sed diam nonummy nibh euismod tincidunt ut laoreet dolor magna aliquam erat volu. Wisi enim ad minim veniam.</div>
  <div class="abs avatar" style="left:163px;top:856px" role="img" aria-label="Portrait photo of patient Clara Whitmore"></div>
  <div class="abs avatar" style="left:366px;top:859px" role="img" aria-label="Portrait photo of patient Nina Ashby"></div>
  <div class="abs avatar" style="left:564px;top:856px" role="img" aria-label="Portrait photo of patient Marcus Fielding"></div>
  <p class="abs who" style="left:44px">Clara Whitmore</p>
  <p class="abs who" style="left:245px">Nina Ashby</p>
  <p class="abs who" style="left:445px">Marcus Fielding</p>
  <div class="abs dots"><span></span><span></span><span></span></div>

  <!-- footer -->
  <footer class="abs footer">
    <div class="abs foot-logo">
      <span class="logo-dot" style="background:var(--purple-soft)"></span>
      <span class="logo-name" style="color:#fff">Harbour Lane<br>Foot Care</span>
    </div>
    <p class="abs foot-head" style="left:169px">QUICK LINKS</p>
    <div class="abs foot-list" style="left:169px;top:51px">Home<br>About Us<br>Services<br>Contact Us<br>Blog</div>
    <p class="abs foot-head" style="left:261px">CONTACT</p>
    <div class="abs foot-item" style="left:261px;top:49px">
      <svg width="11" height="11" viewBox="0 0 14 14"><circle cx="7" cy="7" r="6.3" fill="none" stroke="#fff" stroke-width="1.2"/><path d="M7 3.3a2.4 2.4 0 0 1 2.4 2.4c0 1.8-2.4 4.6-2.4 4.6S4.6 7.5 4.6 5.7A2.4 2.4 0 0 1 7 3.3z" fill="#fff"/></svg>
      <span>Suite 12<br>88 Harbour Lane<br>Melbourne 3000</span>
    </div>
    <div class="abs foot-item" style="left:261px;top:88px">
      <svg width="11" height="11" viewBox="0 0 14 14"><circle cx="7" cy="7" r="6.3" fill="none" stroke="#fff" stroke-width="1.2"/><path d="M4.5 4c.6-.6 1.2-.4 1.5.2l.4.8c.2.4 0 .7-.3 1 .4.9 1 1.5 1.9 1.9.3-.3.6-.5 1-.3l.8.4c.6.3.8.9.2 1.5-1.3 1.2-5.8-3.3-5.5-5.5z" fill="#fff"/></svg>
      <span>1300 555 274</span>
    </div>
    <div class="abs foot-item" style="left:261px;top:108px">
      <svg width="11" height="11" viewBox="0 0 10 10"><circle cx="5" cy="5" r="4.5" fill="none" stroke="#fff"/><rect x="2.5" y="3.3" width="5" height="3.4" fill="none" stroke="#fff" stroke-width=".8"/></svg>
      <span>info@harbourlanefootcare.com</span>
    </div>
    <div class="abs map" role="img" aria-label="Street map of the Melbourne CBD with the clinic location pinned"></div>
  </footer>
  <div class="abs bottombar">COPYRIGHT © 2016 HARBOUR LANE FOOT CARE. ALL RIGHTS RESERVED.</div>
  <div class="abs socials" style="left:632px;top:1168px"><span class="circle-ico" style="background:#fff"></span><span class="circle-ico" style="background:#fff"></span></div>
</div>
</body>
</html>
```